Software as a Service to manage Home Care Management

We need a web site designed for Home Care Management Software as a Service product, that facilitates Home Care organizations to manage and schedule carers to visit client homes. We want a modern look and feel using our existing logo.

Target Market(s)

Home Care Management organizations. Product is similar to: https://kelvantro.co/

Coding

Coded - Design and coding required

Number of Pages Required

3 page

```html
<!DOCTYPE html>
<html lang="en">
<head>
<meta charset="utf-8">
<title>Carelane — Home Care Management Software</title>
<link href="https://fonts.googleapis.com/css2?family=Cinzel:wght@400;600&family=Poppins:wght@400;500;600&display=swap" rel="stylesheet">
<style>
:root{
  --pink:#e8336f;
  --pink-soft:#f7c6d6;
  --ink:#2b2b2b;
  --muted:#6d6d6d;
  --band:#f1f1f1;
  --white:#ffffff;
  --dark:#2a2a2a;
  --darker:#1f1f1f;
}
*{box-sizing:border-box;margin:0;padding:0}
html,body{width:1200px;height:4168px;overflow:hidden}
body{position:relative;background:var(--white);font-family:'Poppins',sans-serif;color:var(--ink)}
.abs{position:absolute}
.heading{font-family:'Cinzel',serif;font-size:34px;font-weight:400;color:var(--ink);text-align:center;letter-spacing:1px}
.heading .accent{color:var(--pink)}
.heading-rule{width:40px;height:3px;background:var(--pink);margin:14px auto 0;border-radius:2px}
.btn{display:inline-block;background:var(--pink);color:var(--white);font-size:14px;font-weight:500;padding:12px 22px;border-radius:4px}
.btn-dark{background:#111;color:var(--white)}
.copy{font-size:14px;line-height:26px;color:var(--muted)}
.lead{font-size:19px;line-height:30px;font-weight:600;color:var(--ink)}

/* header */
.site-header{left:0;top:0;width:1200px;height:72px;background:var(--white);display:flex;align-items:center;justify-content:space-between;padding:0 168px 0 160px;z-index:3}
.brand{display:flex;align-items:center;gap:10px;font-family:'Cinzel',serif;font-size:22px;font-weight:600;color:var(--ink)}
.brand-dot{width:26px;height:26px;border-radius:50%;background:var(--pink)}
.nav{display:flex;align-items:center;gap:34px;font-size:14px}
.nav .btn{padding:10px 20px}

/* hero */
.hero{left:0;top:72px;width:1200px;height:668px}
.hero-photo{position:absolute;inset:0;background:linear-gradient(100deg,#4a4a4a 0%,#6b6664 35%,#b9aca6 60%,#d9cdc6 100%)}
.hero-curve{position:absolute;left:0;bottom:0;width:1200px;height:120px}
.hero-title{left:160px;top:300px;font-family:'Cinzel',serif;font-size:44px;line-height:56px;color:var(--white);letter-spacing:1px}
.hero-cta{left:160px;top:420px}

/* about */
.about-head{left:0;top:808px;width:1200px}
.about-photo{left:160px;top:912px;width:372px;height:370px;border-radius:16px;background:linear-gradient(135deg,#e9e6e2,#cfc8c1 60%,#a89f97)}
.about-text{left:580px;top:930px;width:500px}
.about-text .copy{margin-top:18px}

/* how it works */
.how{left:0;top:1432px;width:1200px;height:480px;background:var(--band)}
.how-head{left:160px;top:1500px;font-family:'Cinzel',serif;font-size:34px;color:var(--ink)}
.how-head .accent{color:var(--pink)}
.how-rule{left:160px;top:1550px;width:40px;height:3px;background:var(--pink)}
.how-lead{left:160px;top:1580px;width:560px}
.how-list{left:160px;top:1670px;width:520px;list-style:none}
.how-list li{display:flex;gap:16px;margin-bottom:22px;font-size:13px;line-height:22px;color:var(--muted)}
.how-list li::before{content:"";flex:0 0 12px;height:12px;margin-top:5px;background:var(--pink);border-radius:2px}
.phone{left:782px;top:1396px;width:258px;height:540px;border-radius:38px;background:#111;padding:14px}
.phone-screen{width:100%;height:100%;border-radius:28px;background:linear-gradient(180deg,#f2d9df,#e3c7cd 55%,#fff 100%);display:flex;flex-direction:column;align-items:center;justify-content:center;gap:14px}
.phone-brand{font-family:'Cinzel',serif;font-size:18px;font-weight:600;color:var(--ink)}
.phone-screen .btn{font-size:11px;padding:8px 16px}

/* why */
.why-head{left:0;top:2032px;width:1200px}
.features{left:160px;top:2150px;width:880px;display:flex;justify-content:space-between}
.feature{width:260px;text-align:center}
.feature-icon{width:96px;height:96px;border-radius:50%;margin:0 auto 22px;display:flex;align-items:center;justify-content:center}
.feature-icon.pink{background:var(--pink)}
.feature-icon.dark{background:#2e2e2e}
.feature h3{font-size:17px;font-weight:600;margin-bottom:10px}
.feature p{font-size:12px;line-height:20px;color:var(--muted)}

/* testimonials */
.testimonials{left:0;top:2432px;width:1200px;height:416px;background:var(--band)}
.testi-head{left:0;top:2500px;width:1200px}
.quote-mark{left:528px;top:2610px;width:64px;height:64px;border-radius:50%;background:var(--pink);color:var(--white);font-family:'Cinzel',serif;font-size:44px;line-height:78px;text-align:center}
.avatar{left:572px;top:2606px;width:68px;height:68px;border-radius:50%;border:3px solid var(--white);background:linear-gradient(135deg,#e8d6cc,#b69a8c)}
.testi-text{left:300px;top:2694px;width:600px;text-align:center;font-size:13px;line-height:22px;color:var(--muted);font-style:italic}
.testi-name{left:0;top:2794px;width:1200px;text-align:center;font-size:16px;font-weight:500}
.arrow{top:2720px;width:24px;height:40px}

/* partners */
.partners-head{left:0;top:2960px;width:1200px}
.partners{left:160px;top:3086px;width:880px;display:flex;justify-content:space-between}
.badge{width:160px;height:84px;background:var(--white);box-shadow:0 6px 18px rgba(0,0,0,.1);display:flex;align-items:center;justify-content:center}
.badge span{display:block;width:96px;height:20px;border-radius:10px;background:#d5d5d5}

/* contact */
.contact{left:0;top:3284px;width:1200px;height:676px;background:var(--band)}
.contact-head{left:0;top:3372px;width:1200px}
.contact-form{left:160px;top:3480px;width:480px;height:400px;background:var(--white);padding:28px 50px}
.field{height:38px;border:1px solid #e1e1e1;border-radius:3px;margin-bottom:16px;font-size:11px;color:#999;padding:11px 14px}
.field-row{display:flex;gap:16px}
.field-row .field{flex:1}
.contact-form .btn{font-size:11px;padding:9px 16px}
.contact-photo{left:760px;top:3440px;width:360px;height:520px;background:linear-gradient(180deg,#e6e9ee,#c3cad3 50%,#5a6a80)}

/* footer */
.site-footer{left:0;top:3960px;width:1200px;height:208px;background:var(--dark);color:var(--white)}
.footer-items{position:absolute;left:160px;top:56px;width:880px;display:flex;justify-content:space-between}
.footer-item{display:flex;gap:16px;align-items:flex-start;width:260px;font-size:13px;line-height:20px}
.footer-item strong{display:block;font-weight:500}
.footer-item small{color:#bdbdbd;font-size:12px}
.footer-icon{flex:0 0 44px;height:44px;border-radius:50%;border:2px solid var(--white);display:flex;align-items:center;justify-content:center}
.footer-bar{position:absolute;left:0;bottom:0;width:1200px;height:52px;background:var(--darker);display:flex;align-items:center;justify-content:space-between;padding:0 160px;font-size:11px;color:#bbb}
.socials{display:flex;gap:10px}
.socials span{width:22px;height:22px;border-radius:50%;background:var(--white)}
.socials span:first-child{background:var(--pink)}
</style>
</head>
<body>

<header class="site-header abs">
  <div class="brand"><span class="brand-dot"></span>Carelane</div>
  <nav class="nav">
    <span>About Us</span><span>Our Products</span><span>Contact Us</span>
    <span class="btn">Book A Free Demo</span>
  </nav>
</header>

<section class="hero abs">
  <div class="hero-photo" role="img" aria-label="Photo of a smiling carer embracing an elderly woman at home"></div>
  <svg class="hero-curve" viewBox="0 0 1200 120" preserveAspectRatio="none">
    <path d="M0 20 Q600 150 1200 20 L1200 120 L0 120 Z" fill="var(--pink)"/>
    <path d="M0 40 Q600 150 1200 40 L1200 120 L0 120 Z" fill="#fff"/>
  </svg>
</section>
<h1 class="hero-title abs">We Provide Home Care<br>Management Software</h1>
<span class="hero-cta btn abs">Book A Free Demo</span>

<div class="about-head abs">
  <h2 class="heading"><span class="accent">About</span> Carelane</h2>
  <div class="heading-rule"></div>
</div>
<div class="about-photo abs" role="img" aria-label="Photo of a businesswoman working on a laptop"></div>
<div class="about-text abs">
  <p class="lead">Lorem ipsum dolor sit amet, consectetur adipiscing elit, sed do eiusmod tempor ut labore et dolore magna aliqua.</p>
  <p class="copy">Ut enim ad minim veniam, quis nostrud exercitation ullamco laboris nisi ut aliquip ex ea commodo consequat. Duis aute irure dolor in reprehenderit in voluptate velit esse cillum dolore eu fugiat nulla pariatur. Excepteur sint occaecat cupidatat non proident, sunt in culpa qui officia deserunt mollit anim id est laborum.</p>
  <p class="copy">Sed ut perspiciatis unde omnis iste natus error sit voluptatem accusantium doloremque laudantium, totam rem aperiam, eaque ipsa quae ab illo inventore veritatis et quasi architecto beatae vitae dicta sunt explicabo. Nemo enim ipsam voluptatem quia voluptas sit aspernatur aut odit aut fugit, sed quia consequuntur magni dolores eos qui ratione.</p>
</div>

<section class="how abs"></section>
<h2 class="how-head abs"><span class="accent">How</span> It Works</h2>
<div class="how-rule abs"></div>
<p class="how-lead lead abs">Lorem ipsum dolor sit amet, consectetur adipiscing elit, sed do eiusmod tempor ut labore et dolore magna aliqua.</p>
<ul class="how-list abs">
  <li>Ut enim ad minim veniam, quis nostrud exercitation ullamco laboris nisi ut aliquip ex ea commodo consequat.</li>
  <li>Ut enim ad minim veniam, quis nostrud exercitation ullamco laboris nisi ut aliquip ex ea commodo consequat.</li>
  <li>Ut enim ad minim veniam, quis nostrud exercitation ullamco laboris nisi ut aliquip ex ea commodo consequat.</li>
  <li>Ut enim ad minim veniam, quis nostrud exercitation ullamco laboris nisi ut aliquip ex ea commodo consequat.</li>
</ul>
<div class="phone abs">
  <div class="phone-screen">
    <div class="phone-brand">Carelane</div>
    <span class="btn">Book A Free Demo</span>
    <span class="btn btn-dark">Contact Us Today</span>
  </div>
</div>

<div class="why-head abs">
  <h2 class="heading"><span class="accent">Why</span> Carelane</h2>
  <div class="heading-rule"></div>
</div>
<div class="features abs">
  <div class="feature">
    <div class="feature-icon pink">
      <svg width="44" height="44" viewBox="0 0 44 44" fill="none" stroke="#fff" stroke-width="3"><circle cx="22" cy="14" r="7"/><path d="M8 38c0-8 6-13 14-13s14 5 14 13"/></svg>
    </div>
    <h3>Dedicated Team</h3>
    <p>Ut enim ad minim veniam, quis nostrud exercitation ullamco laboris nisi ut aliquip ex ea commodo consequat.</p>
  </div>
  <div class="feature">
    <div class="feature-icon dark">
      <svg width="44" height="44" viewBox="0 0 44 44" fill="none" stroke="#fff" stroke-width="3"><circle cx="22" cy="18" r="11"/><path d="M15 28l-3 12 10-5 10 5-3-12"/></svg>
    </div>
    <h3>Best Product</h3>
    <p>Ut enim ad minim veniam, quis nostrud exercitation ullamco laboris nisi ut aliquip ex ea commodo consequat.</p>
  </div>
  <div class="feature">
    <div class="feature-icon dark">
      <svg width="44" height="44" viewBox="0 0 44 44" fill="none" stroke="#fff" stroke-width="3"><rect x="7" y="10" width="30" height="27" rx="3"/><path d="M7 18h30M15 6v8M29 6v8M16 27l4 4 8-8"/></svg>
    </div>
    <h3>Manage Schedule</h3>
    <p>Ut enim ad minim veniam, quis nostrud exercitation ullamco laboris nisi ut aliquip ex ea commodo consequat.</p>
  </div>
</div>

<section class="testimonials abs"></section>
<div class="testi-head abs">
  <h2 class="heading"><span class="accent">Manager</span> Testimonials</h2>
  <div class="heading-rule"></div>
</div>
<div class="quote-mark abs">“</div>
<div class="avatar abs" role="img" aria-label="Portrait photo of the reviewing manager"></div>
<p class="testi-text abs">Lorem ipsum dolor sit amet, consectetur adipiscing elit, sed diam nonummy nibh euismod tincidunt ut laoreet dolore magna aliquam erat volutpat. Ut wisi enim ad minim veniam, quis nostrud exerci tation ullamcorper suscipit lobortis nisl ut aliquip ex ea commodo consequat. Duis autem vel eum iriure dolor in hendrerit in vulputate velit esse molestie consequat illum.</p>
<p class="testi-name abs">– Dana Whitlow, Leeds</p>
<svg class="arrow abs" style="left:110px" viewBox="0 0 24 40" fill="none" stroke="var(--pink)" stroke-width="3"><path d="M20 4L4 20l16 16"/></svg>
<svg class="arrow abs" style="left:1066px" viewBox="0 0 24 40" fill="none" stroke="var(--pink)" stroke-width="3"><path d="M4 4l16 16L4 36"/></svg>

<div class="partners-head abs">
  <h2 class="heading"><span class="accent">Working</span> In Association With</h2>
  <div class="heading-rule"></div>
</div>
<div class="partners abs">
  <div class="badge"><span></span></div>
  <div class="badge"><span></span></div>
  <div class="badge"><span></span></div>
  <div class="badge"><span></span></div>
  <div class="badge"><span></span></div>
</div>

<section class="contact abs"></section>
<div class="contact-head abs">
  <h2 class="heading"><span class="accent">Get</span> In Touch</h2>
  <div class="heading-rule"></div>
</div>
<form class="contact-form abs">
  <div class="field">Name*</div>
  <div class="field">Company Name*</div>
  <div class="field">Phone*</div>
  <div class="field">Email*</div>
  <div class="field-row"><div class="field">dd / mm / yyyy</div><div class="field">Select Time</div></div>
  <span class="btn">Book Now</span>
</form>
<div class="contact-photo abs" role="img" aria-label="Photo of a smiling man in a shirt and tie holding a laptop"></div>

<footer class="site-footer abs">
  <div class="footer-items">
    <div class="footer-item">
      <span class="footer-icon"><svg width="18" height="22" viewBox="0 0 18 22" fill="none" stroke="#fff" stroke-width="2"><path d="M9 21s7-7 7-12A7 7 0 0 0 2 9c0 5 7 12 7 12z"/><circle cx="9" cy="9" r="2.5"/></svg></span>
      <div><strong>Carelane</strong><small>123, Lorem Ipsum Dolor, Sit Amet, Consectetur</small></div>
    </div>
    <div class="footer-item">
      <span class="footer-icon"><svg width="20" height="20" viewBox="0 0 20 20" fill="none" stroke="#fff" stroke-width="2"><path d="M4 2h4l2 5-3 2a11 11 0 0 0 4 4l2-3 5 2v4a2 2 0 0 1-2 2A16 16 0 0 1 2 4a2 2 0 0 1 2-2z"/></svg></span>
      <div><strong>Call Us</strong><span style="font-size:18px">(555) 014 2290</span></div>
    </div>
    <div class="footer-item">
      <span class="footer-icon"><svg width="20" height="16" viewBox="0 0 20 16" fill="none" stroke="#fff" stroke-width="2"><rect x="1" y="1" width="18" height="14" rx="2"/><path d="M1 3l9 6 9-6"/></svg></span>
      <div><strong>Email Us</strong><small>hello@carelane.co</small></div>
    </div>
  </div>
  <div class="footer-bar">
    <span>© 2020 Carelane. All Rights Reserved.</span>
    <div class="socials"><span></span><span></span><span></span></div>
  </div>
</footer>

</body>
</html>
```